RKT Capability Statement Brochure

We need a four or six-page flyer/brochure for our capability statement. This should include all the key written copy and photos/descriptions of the personnel, plus contact addresses in the current capability statement which is attached. We are looking for a modern, professional design that matches our professional approach to our business. Please incorporate our logo into the design.

Target Market(s)

Government departments, shipping companies, port operators, lawyers, export and import businesses, commodity companies.

Industry/Entity Type

Business Consultant

Contact Information for Business Card

Professional, simple to read, uncomplicated.

Font styles to use
Serif
Sans Serif

Colors

Designer to choose colors to be used in the design.

Requirements
Must have
• Company logo
• KEY MESSAGE: Providing independent, expert, confidential and professional services.
• Description of company
• Description and photos of personnel.
• Contact details.
Should not have
• No cliches

```html
<!DOCTYPE html>
<html lang="en">
<head>
<meta charset="utf-8">
<title>RKT Capability Statement 2018</title>
<link href="https://fonts.googleapis.com/css2?family=Roboto:wght@400;500;700;900&display=swap" rel="stylesheet">
<style>
:root{
  --backdrop:#b3d6de;
  --navy:#1c3d78;
  --deep:#132c5a;
  --accent:#2f8fd8;
  --ink:#3a4556;
  --paper:#ffffff;
  --sky-top:#c9dcea;
  --sea:#1f4d6b;
}
*{box-sizing:border-box;margin:0;padding:0}
html,body{width:1200px;height:1200px;overflow:hidden}
body{background:var(--backdrop);font-family:"Roboto",Arial,sans-serif;color:var(--ink);position:relative}
.board-title{position:absolute;left:90px;top:40px;font-size:32px;font-weight:700;color:var(--navy);letter-spacing:.5px}
.page{position:absolute;width:300px;height:424px;background:var(--paper);box-shadow:0 3px 10px rgba(20,50,80,.25);overflow:hidden}
.p1{left:90px;top:110px}.p2{left:450px;top:110px}.p3{left:810px;top:110px}
.p4{left:90px;top:620px}.p5{left:450px;top:620px}.p6{left:810px;top:620px}
.page-header{position:absolute;right:0;top:0;width:300px;height:22px}
.page-header .tag{position:absolute;right:10px;top:4px;font-size:4.5px;line-height:1.3;color:#fff;text-align:right;font-weight:500}
.page-footer{position:absolute;left:0;bottom:0;width:100%;height:16px;background:var(--navy);display:flex;align-items:center;gap:14px;padding:0 12px;color:#fff;font-size:4.5px}
.page-footer .mark{font-weight:900;font-size:9px;letter-spacing:.3px}
.page-footer .num{margin-left:auto}
.content{position:absolute;left:22px;right:22px;top:40px}
h2{font-size:7px;font-weight:700;color:var(--deep);margin-bottom:6px;text-transform:uppercase}
h3{font-size:5.6px;font-weight:700;color:var(--accent);margin:7px 0 3px;text-transform:uppercase;display:flex;align-items:center;gap:4px}
p,li{font-size:4.8px;line-height:1.5}
p{margin-bottom:4px}
ul{list-style:none;padding-left:8px}
li::before{content:"•";color:var(--navy);margin-left:-5px;margin-right:3px}
.icon{width:8px;height:8px}
.cover-name{position:absolute;left:0;right:0;top:26px;text-align:center}
.cover-name .word{font-size:44px;font-weight:900;color:var(--navy);line-height:1}
.cover-name .full{font-size:7px;color:var(--accent);letter-spacing:1.4px;margin-top:2px}
.key-message{position:absolute;left:0;right:0;top:96px;text-align:center;font-size:7.2px;line-height:1.4;color:var(--ink)}
.cover-photo{position:absolute;left:40px;top:130px;width:220px;height:210px;border-radius:70px 70px 70px 70px/60px 60px 60px 60px;background:linear-gradient(180deg,var(--sky-top) 0%,#e8eff5 48%,#3d6c8a 52%,var(--sea) 100%)}
.cover-title{position:absolute;left:0;right:0;top:356px;text-align:center;font-weight:700;color:var(--navy);font-size:13px;line-height:1.25}
.member{display:flex;gap:6px;margin-bottom:8px}
.portrait{flex:0 0 34px;height:40px;background:linear-gradient(160deg,#c7ccd3,#7c8694)}
.member .name{font-size:5.2px;font-weight:700;color:var(--deep);margin-bottom:2px}
.intro-band{position:absolute;left:0;right:0;top:22px;height:58px;display:flex;gap:8px;padding:10px 14px 0}
.ship-photo{flex:0 0 78px;height:42px;background:linear-gradient(180deg,#dfe7ee,#8aa2b8 60%,#2c4a66)}
.intro-band p{font-size:5px;font-weight:700;color:var(--deep)}
.contacts-band{position:absolute;left:0;right:0;top:82px;height:236px;background:var(--navy);color:#fff}
.contacts-band h2{color:#fff;text-align:center;margin-top:8px}
.map{margin:0 auto;width:200px;height:70px;background:linear-gradient(90deg,#24498a,#2d5aa0,#24498a);border-radius:4px}
.regions{display:grid;grid-template-columns:1fr 1fr;gap:8px 16px;padding:10px 22px}
.region .state{font-size:5px;color:#6fb8ef;font-weight:700;margin-bottom:2px}
.region .who{font-size:5.2px;font-weight:700}
.region .line{font-size:4.6px;line-height:1.45;color:#dbe6f5}
.address-band{position:absolute;left:0;right:0;top:326px;display:flex;padding:0 16px;gap:14px}
.address-band .word{font-size:26px;font-weight:900;color:var(--navy);line-height:1}
.address-band .full{font-size:5px;color:var(--accent);letter-spacing:.8px}
.address-band .entity{font-size:4.6px;line-height:1.45;margin-top:4px;font-weight:500}
.address-band .reg h3{margin-top:0}
.address-band .reg div{font-size:4.6px;line-height:1.45}
</style>
</head>
<body>
<div class="board-title">DESIGN IDEA - 02</div>

<section class="page p1">
  <div class="cover-name">
    <div class="word">RKT</div>
    <div class="full">ROCKPORT MARITIME GROUP</div>
  </div>
  <div class="key-message">Providing independent, expert,<br>confidential and professional services</div>
  <div class="cover-photo" role="img" aria-label="Photograph of open sea beneath a cloudy sky"></div>
  <div class="cover-title">CAPABILITY STATEMENT<br>2018</div>
</section>

<section class="page p2">
  <svg class="page-header" viewBox="0 0 300 22" aria-hidden="true"><polygon points="0,0 300,0 300,22 40,22" fill="var(--deep)"/><polygon points="0,0 40,22 0,22" fill="var(--paper)"/></svg>
  <div class="page-header"><div class="tag">Independent Harbour Advisory<br>Commercial Shipping Consultants</div></div>
  <div class="content">
    <h2>Company Overview</h2>
    <p>Established in 2009, Rockport Maritime Group has offices in Victoria, New South Wales, Queensland and Tasmania and aims to be the leading maritime consultancy in the region.</p>
    <p>The team brings together extensive commercial experience and expertise to deliver a highly focused approach to every technical and operational analysis it undertakes for clients.</p>
    <p>We hold an international network of associates, including strategic partnerships with global ports and shipping data analysts, to support our clients in any trade.</p>
    <p>Our services cover shipping, transportation and marine industry expertise, from feasibility studies to vessel acquisition, chartering, port planning and dispute support.</p>
    <p>We are able to step in to a client's existing organisation and supply the skill, knowledge and services to supplement or support a running operation or project.</p>
    <p>The group is a member of the leading freight and trade alliances and its principals hold accreditation with recognised maritime institutes.</p>
    <p>You can count on our professional team to expertly cater to all of your commercial maritime requirements, in confidence and with independent advice.</p>
  </div>
  <footer class="page-footer"><span class="mark">RKT</span><span>+61 3 9000 0000</span><span>info@rockportmaritime.example</span><span class="num">02 | Page</span></footer>
</section>

<section class="page p3">
  <svg class="page-header" viewBox="0 0 300 22" aria-hidden="true"><polygon points="40,0 300,0 300,22 80,22" fill="var(--deep)"/></svg>
  <div class="page-header"><div class="tag">Independent Harbour Advisory<br>Commercial Shipping Consultants</div></div>
  <div class="content">
    <h2>Core Competencies</h2>
    <p>RKT has demonstrable experience in the following areas:</p>
    <h3><svg class="icon" viewBox="0 0 10 10"><rect x="1" y="1" width="8" height="8" fill="none" stroke="var(--navy)"/></svg>Commercial Maritime Trade</h3>
    <ul>
      <li>Operational knowledge of all shipping trades</li>
      <li>Understanding of charter party and logistics</li>
      <li>Review of commercial maritime operations</li>
      <li>Evaluation of tenders and proposal preparation</li>
      <li>Feasibility studies for new trade services</li>
      <li>Advice on joint venture and fleet issues</li>
      <li>Industry education and tailored training</li>
    </ul>
    <h3><svg class="icon" viewBox="0 0 10 10"><path d="M1 7h8l-2 2H3z M5 1v6" fill="none" stroke="var(--navy)"/></svg>Ship Management</h3>
    <ul>
      <li>Vessel ownership and management review</li>
      <li>Vessel chartering and operational planning</li>
      <li>Vessel sales and purchase advice</li>
      <li>Crewing and manning arrangements</li>
      <li>Compliance with maritime safety systems</li>
      <li>Management of supplier and repair contracts</li>
      <li>Insurance and claims handling support</li>
    </ul>
    <h3><svg class="icon" viewBox="0 0 10 10"><path d="M1 9V4l4-3 4 3v5z" fill="none" stroke="var(--navy)"/></svg>Ports &amp; Related Industry</h3>
    <ul>
      <li>Port planning and throughput modelling</li>
      <li>Berth capacity and cargo handling studies</li>
      <li>Port efficiency and productivity reviews</li>
      <li>Forecasting of cargo volumes and pricing</li>
      <li>Tariff and port charge assessments</li>
      <li>Emergency and crisis management planning</li>
    </ul>
  </div>
  <footer class="page-footer"><span class="mark">RKT</span><span>+61 3 9000 0000</span><span>info@rockportmaritime.example</span><span class="num">03 | Page</span></footer>
</section>

<section class="page p4">
  <svg class="page-header" viewBox="0 0 300 22" aria-hidden="true"><polygon points="40,0 300,0 300,22 80,22" fill="var(--deep)"/></svg>
  <div class="page-header"><div class="tag">Independent Harbour Advisory<br>Commercial Shipping Consultants</div></div>
  <div class="content">
    <h3 style="margin-top:0"><svg class="icon" viewBox="0 0 10 10"><circle cx="5" cy="5" r="4" fill="none" stroke="var(--navy)"/></svg>Supply Chain</h3>
    <ul>
      <li>Supply chain evaluation and optimisation</li>
      <li>Evaluation and management of tenders</li>
      <li>Marine project management and support</li>
      <li>Management of bulk and breakbulk logistics</li>
      <li>Stocking analysis for bulk terminals</li>
    </ul>
    <h2 style="margin-top:10px">Rockport Maritime Group Team</h2>
    <p>All team members have decades of commercial shipping industry experience at senior levels and have substantial relevant specialist expertise to offer across ports, trade, operations and fleet management.</p>
    <p>The RKT management team comprises:</p>
    <div class="member">
      <div class="portrait" role="img" aria-label="Portrait photo of Owen Pritchard"></div>
      <div><div class="name">Owen Pritchard</div><p>Based in Sydney, Owen was a general manager with a major liner group for many years. His work covered fleet planning, terminal contracts and trade development across the Pacific and Asian regions.</p></div>
    </div>
    <div class="member">
      <div class="portrait" role="img" aria-label="Portrait photo of Fiona Cairns"></div>
      <div><div class="name">Fiona Cairns</div><p>Based in Melbourne, Fiona has more than thirty years of experience in the international maritime and transport industries, including senior roles in port authorities, chartering and shipping finance.</p></div>
    </div>
  </div>
  <footer class="page-footer"><span class="mark">RKT</span><span>+61 3 9000 0000</span><span>info@rockportmaritime.example</span><span class="num">04 | Page</span></footer>
</section>

<section class="page p5">
  <svg class="page-header" viewBox="0 0 300 22" aria-hidden="true"><polygon points="40,0 300,0 300,22 80,22" fill="var(--deep)"/></svg>
  <div class="page-header"><div class="tag">Independent Harbour Advisory<br>Commercial Shipping Consultants</div></div>
  <div class="content">
    <div class="member">
      <div class="portrait" role="img" aria-label="Portrait photo of Martin Hale"></div>
      <div><div class="name">Martin Hale</div><p>Based in Melbourne, Martin is a master mariner and holds an advanced business qualification. A founding member of RKT, he has led commercial operations and strategic development for shipping lines and port groups.</p></div>
    </div>
    <div class="member">
      <div class="portrait" role="img" aria-label="Portrait photo of Daniel Moore"></div>
      <div><div class="name">Daniel Moore</div><p>Based in Hobart, Daniel commenced his maritime career as a deck officer and gained broad experience in ferry, offshore and bulk sectors. He now advises on safety systems and fleet operations.</p></div>
    </div>
    <div class="member">
      <div class="portrait" role="img" aria-label="Portrait photo of Gavin Ashby"></div>
      <div><div class="name">Gavin Ashby</div><p>Based in Brisbane, Gavin has a seafaring background and over forty years in commercial shipping. He has founded ship agencies, managed vessel sales and advised government on port projects.</p></div>
    </div>
    <h2 style="margin-top:6px">Clients</h2>
    <p>RKT clients include government agencies, most of the major resource companies, ports and shipping operators. Our team has earned the confidence of several Commonwealth departments and regional bodies through careful independent work.</p>
  </div>
  <footer class="page-footer"><span class="mark">RKT</span><span>+61 3 9000 0000</span><span>info@rockportmaritime.example</span><span class="num">05 | Page</span></footer>
</section>

<section class="page p6">
  <svg class="page-header" viewBox="0 0 300 22" aria-hidden="true"><polygon points="40,0 300,0 300,22 80,22" fill="var(--deep)"/></svg>
  <div class="page-header"><div class="tag">Independent Harbour Advisory<br>Commercial Shipping Consultants</div></div>
  <div class="intro-band">
    <div class="ship-photo" role="img" aria-label="Photograph of an offshore support vessel at sea"></div>
    <p>RKT has acted as broker for significant multi-million-dollar ship acquisitions for the nation and provided advice and analysis on projects ranging from market research through to sale of surplus defence marine assets.</p>
  </div>
  <div class="contacts-band">
    <h2>Contacts</h2>
    <div class="map" role="img" aria-label="World map highlighting Australia"></div>
    <div class="regions">
      <div class="region"><div class="state">Victoria</div><div class="who">Martin Hale</div><div class="line">Tel: +61 400 111 201<br>martin@rockportmaritime.example</div>
        <div class="who" style="margin-top:4px">Fiona Cairns</div><div class="line">Tel: +61 400 111 202<br>fiona@rockportmaritime.example</div></div>
      <div class="region"><div class="state">Queensland</div><div class="who">Gavin Ashby</div><div class="line">Tel: +61 400 111 203<br>gavin@rockportmaritime.example</div>
        <div class="state" style="margin-top:6px">Tasmania</div><div class="who">Daniel Moore</div><div class="line">Tel: +61 400 111 204<br>daniel@rockportmaritime.example</div></div>
      <div class="region"><div class="state">New South Wales</div><div class="who">Owen Pritchard</div><div class="line">Tel: +61 400 111 205<br>owen@rockportmaritime.example</div></div>
    </div>
  </div>
  <div class="address-band">
    <div>
      <div class="word">RKT</div>
      <div class="full">ROCKPORT MARITIME GROUP</div>
      <div class="entity">Rockport Maritime Group Pty Ltd<br>ATF RKT Group Unit Trust<br>ABN 00 000 000 000</div>
    </div>
    <div class="reg">
      <h3>Registered Address</h3>
      <div>Rockport Maritime Group Pty Ltd<br>42 Harbour View Road<br>Westbay, Victoria 3999</div>
      <div style="margin-top:3px"><b>Telephone:</b> +61 3 9000 0000 <b>Fax:</b> +61 3 9000 0001<br><b>Email:</b> info@rockportmaritime.example</div>
    </div>
  </div>
</section>
</body>
</html>
```